wine label

Label for wine, in black and silver, format to be in PDF ,EPS, PSD Label to be split main label to have Name: Morbray Ash family crest, dry grown, and Clare Valley
other section to have the type of wine ie: Grenache and year of harvest.
Some ideas we had our enclosed

```html
<!DOCTYPE html>
<html lang="en">
<head>
<meta charset="utf-8">
<title>Morbray Ash Grenache 2012 – Wine Label</title>
<link rel="stylesheet" href="https://fonts.googleapis.com/css2?family=Open+Sans:wght@400;600;700;800&display=swap">
<style>
  :root {
    --backdrop: #1b1b1c;
    --label-black: #151515;
    --label-sheen: #262626;
    --silver-light: #f0f0f0;
    --silver-mid: #cfcfcf;
    --silver-dark: #a8a8a8;
    --ink-dark: #1a1a1a;
  }
  html, body {
    margin: 0;
    padding: 0;
    width: 1200px;
    height: 1148px;
    overflow: hidden;
    background: var(--backdrop);
  }
  .canvas {
    position: relative;
    width: 1200px;
    height: 1148px;
    background: var(--backdrop);
  }
  .wine-label {
    position: absolute;
    left: 379px;
    top: 144px;
    width: 482px;
    height: 878px;
    background:
      repeating-linear-gradient(180deg, rgba(255,255,255,0.025) 0 1px, transparent 1px 3px),
      linear-gradient(180deg, var(--label-sheen) 0%, var(--label-black) 45%, var(--label-sheen) 100%);
    font-family: "Open Sans", sans-serif;
    color: var(--silver-light);
  }
  .crest-area {
    position: absolute;
    left: 0;
    right: 0;
    top: 190px;
    display: flex;
    flex-direction: column;
    align-items: center;
    text-align: center;
  }
  .crest-disc {
    width: 160px;
    height: 160px;
    border-radius: 50%;
    background: radial-gradient(circle at 40% 35%, var(--silver-light), var(--silver-mid) 70%, var(--silver-dark));
  }
  .brand-name {
    margin: 26px 0 0;
    font-size: 50px;
    font-weight: 800;
    letter-spacing: 2px;
    line-height: 1;
    text-transform: uppercase;
    color: var(--silver-light);
  }
  .tagline {
    margin: 22px 0 0;
    font-size: 18px;
    font-weight: 700;
    letter-spacing: 0.5px;
    text-transform: uppercase;
    color: var(--silver-light);
    line-height: 1.5;
  }
  .variety-band {
    position: absolute;
    left: 3px;
    right: 3px;
    top: 648px;
    height: 48px;
    background: linear-gradient(90deg, var(--silver-dark), var(--silver-light) 35%, var(--silver-mid) 70%, var(--silver-light));
    display: flex;
    align-items: center;
    justify-content: center;
  }
  .variety {
    margin: 0;
    font-size: 28px;
    font-weight: 700;
    letter-spacing: 6px;
    color: var(--ink-dark);
  }
  .vintage {
    position: absolute;
    left: 0;
    right: 0;
    top: 822px;
    margin: 0;
    text-align: center;
    font-size: 25px;
    font-weight: 600;
    letter-spacing: 4px;
    color: var(--silver-light);
  }
</style>
</head>
<body>
  <main class="canvas">
    <section class="wine-label" aria-label="Morbray Ash Grenache 2012 label">
      <div class="crest-area">
        <div class="crest-disc"></div>
        <h1 class="brand-name">Morbray Ash</h1>
        <p class="tagline">Family Crest, Dry Grown,<br>and Clare Valley</p>
      </div>
      <div class="variety-band">
        <h2 class="variety">GRENACHE</h2>
      </div>
      <p class="vintage">2012</p>
    </section>
  </main>
</body>
</html>
```